Car transport business

We need a new business card design. Attached is our old card sample. I would just like to adjust the logo colors (blue and red) to be brighter. I changed my name to the brighter red and the word dispatcher to a brighter blue as an example. But you can adjust those colors further. And then perhaps you can use the same colors for the card design but use your imagination.

As a suggestion so the card stands out I would like to add a clip art of car carrier truck. Attached are examples of that as well

```html
<!DOCTYPE html>
<html lang="en">
<head>
<meta charset="utf-8">
<title>Vantage Haul – Business Card</title>
<link href="https://fonts.googleapis.com/css2?family=Open+Sans:wght@400;600;700;800&display=swap" rel="stylesheet">
<style>
  :root {
    --stage: #e2e2e2;
    --stage-light: #ececec;
    --brand-blue: #05498a;
    --brand-red: #d71a2c;
    --paper: #f4f4f4;
    --white: #ffffff;
    --truck-tone: #2a68a6;
  }
  * { margin: 0; padding: 0; box-sizing: border-box; }
  html, body { width: 1200px; height: 960px; overflow: hidden; }
  body {
    position: relative;
    background: radial-gradient(ellipse at center, var(--stage-light) 0%, var(--stage) 75%);
    font-family: "Open Sans", Arial, sans-serif;
  }
  .card {
    position: absolute;
    left: 305px;
    width: 592px;
    height: 339px;
    overflow: hidden;
  }
  .card-front { top: 118px; background: var(--brand-blue); }
  .card-back { top: 510px; background: var(--paper); }

  .brand {
    position: absolute;
    display: flex;
    align-items: center;
    gap: 14px;
  }
  .brand-dot {
    width: 38px; height: 38px; border-radius: 50%;
    background: var(--brand-red);
    flex: none;
  }
  .brand-name {
    font-weight: 800;
    font-size: 38px;
    letter-spacing: 1px;
    line-height: 1;
    white-space: nowrap;
  }
  .brand-tagline {
    position: absolute;
    font-weight: 700;
    letter-spacing: 1.6px;
    white-space: nowrap;
  }
  .card-front .brand { left: 88px; top: 155px; }
  .card-front .brand-name { color: var(--white); }
  .card-front .brand-tagline { left: 140px; top: 194px; font-size: 13px; color: var(--white); }

  .card-back .brand { left: 50px; top: 72px; }
  .card-back .brand-dot { width: 32px; height: 32px; }
  .card-back .brand-name { font-size: 32px; color: var(--brand-blue); }
  .card-back .brand-tagline { left: 96px; top: 109px; font-size: 11.5px; color: var(--brand-blue); letter-spacing: 1.3px; }

  .swoosh { position: absolute; inset: 0; }

  .holder { position: absolute; left: 47px; top: 172px; }
  .holder-name { font-weight: 800; font-size: 23px; color: var(--brand-blue); letter-spacing: 0.3px; line-height: 1.1; }
  .holder-role { font-weight: 700; font-size: 14px; color: var(--brand-red); margin-top: 3px; }

  .contacts { position: absolute; left: 47px; top: 242px; list-style: none; }
  .contacts li {
    display: flex; align-items: center; gap: 5px;
    font-size: 15px; color: var(--brand-blue); line-height: 20px;
  }
  .contacts svg { width: 13px; height: 13px; flex: none; }
</style>
</head>
<body>

<section class="card card-front">
  <div class="brand">
    <span class="brand-dot"></span>
    <span class="brand-name">VANTAGE HAUL</span>
  </div>
  <div class="brand-tagline">VEHICLE SHIPPING DONE WITH CARE</div>
</section>

<section class="card card-back">
  <svg class="swoosh" viewBox="0 0 592 339" width="592" height="339">
    <defs>
      <clipPath id="blue-field">
        <path d="M592 22 Q566 262 292 339 L592 339 Z"/>
      </clipPath>
      <linearGradient id="truck-fade" x1="0" y1="0" x2="1" y2="0">
        <stop offset="0" stop-color="var(--truck-tone)" stop-opacity="0.2"/>
        <stop offset="1" stop-color="var(--truck-tone)" stop-opacity="0.75"/>
      </linearGradient>
    </defs>
    <path d="M592 22 Q566 262 292 339 L592 339 Z" fill="var(--brand-blue)"/>
    <g clip-path="url(#blue-field)">
      <rect role="img" aria-label="Car carrier truck loaded with cars" x="380" y="222" width="205" height="105" rx="4" fill="url(#truck-fade)"/>
    </g>
    <path d="M580 42 Q520 262 225 339 L262 339 Q552 258 586 38 Z" fill="var(--brand-red)"/>
  </svg>

  <div class="brand">
    <span class="brand-dot"></span>
    <span class="brand-name">VANTAGE HAUL</span>
  </div>
  <div class="brand-tagline">VEHICLE SHIPPING DONE WITH CARE</div>

  <div class="holder">
    <div class="holder-name">OMAR REYES</div>
    <div class="holder-role">DISPATCHER</div>
  </div>

  <ul class="contacts">
    <li>
      <svg viewBox="0 0 16 16"><path d="M3 1.5l3 .5 1 3-1.8 1.3a9 9 0 0 0 4.5 4.5L11 9l3 1 .5 3-2 1.5C7 14 2 9 1.5 3.5z" fill="var(--brand-red)"/></svg>
      555-201-4470
    </li>
    <li>
      <svg viewBox="0 0 16 16"><rect x="4" y="1.5" width="8" height="4" fill="var(--brand-red)"/><rect x="1" y="6" width="14" height="6" rx="1" fill="var(--brand-red)"/><rect x="4" y="10" width="8" height="4.5" fill="var(--brand-red)"/></svg>
      555-201-4471
    </li>
    <li>
      <svg viewBox="0 0 16 16"><rect x="1" y="3" width="14" height="10" fill="none" stroke="var(--brand-red)" stroke-width="1.8"/><path d="M1.5 3.5L8 9l6.5-5.5" fill="none" stroke="var(--brand-red)" stroke-width="1.8"/></svg>
      vantagehaulco@mail.com
    </li>
  </ul>
</section>

</body>
</html>
```